Lower Cost Storage Scheme Email marketing campaign for Corvel Energy

Design a visually engaging and professional marketing email to promote the upcoming Federal Government Battery Subsidy to our existing solar clients, encouraging them to install a battery system now to maximise savings. email content example "Subject: ⚡ Federal Government Battery Subsidy is Coming – Maximise Your Solar Savings

Body:
Hi [First Name],

Great news! With the federal election now decided, the Federal Government’s Home Battery Subsidy Program is officially on the way.

While the scheme hasn’t formally launched yet, it's guaranteed—and like the solar rebate before it, the subsidy reduces each year, so the earlier you install, the more you’ll save.

Crucially, the subsidy is only available once per household, so it makes sense to install a system that fully meets your home's battery needs right from the start.

Why add a battery to your existing solar system now?
✅ Store your excess solar energy instead of sending it back to the grid for low feed-in tariffs
✅ Use your stored solar power at night, when electricity prices are highest (typically 5–8pm)
✅ Slash your power bills and avoid rising time-of-use charges
✅ Protect your home from power outages
✅ Increase your self-sufficiency and long-term energy security

If you’ve already installed solar with us, now is the ideal time to complete your setup with a battery system designed to maximise your return—and take full advantage of this one-off federal subsidy.

Call us today or reply to this email to secure your spot and beat the rush.

Let your solar work smarter for your home,
The Corvel Energy Team"

Target Market(s)

Content: We’ve provided the copy (see attached or below). The key points to emphasise in the design are: The urgency (subsidy winds down each year, limited to one per household). The benefits of installing a battery now, including energy savings, time-of-use charge avoidance, and self-sufficiency. Call to action: “Call us today or reply to this email to secure your spot and beat the rush.”

Industry/Entity Type

Renewable Energy

Colors
0054AA
0677BA
7BADD7
CADEEF
E8F1F8
EB3D1F
EC4F4E
F09395
F8D3D4
FCEDEE

Requirements
Must have
• Clean, modern, and trustworthy – aligned with Corvel Energy branding. Bold headers and icons to make key points stand out. Include visual elements such as: A solar battery image Infographic or icon-style section showing key battery benefits (e.g. bill savings, backup power, self-consumption) Highlighted call-to-action button (“Secure My Battery Now” or “Beat the Rush”)
Nice to have
• I would like to have our company imagery (Corvel Energy) alongside the battery brands we offer being Velto, QMP, Brimlite and TervoPWR
Should not have
• Unsure

```html
<!DOCTYPE html>
<html lang="en">
<head>
<meta charset="utf-8">
<title>Corvel Energy – Federal Battery Subsidy</title>
<link href="https://fonts.googleapis.com/css2?family=Montserrat:wght@500;600;700&family=Quicksand:wght@400;500;600&display=swap" rel="stylesheet">
<style>
:root{
  --blue:#0054AA;
  --blue-mid:#0677BA;
  --blue-soft:#7BADD7;
  --blue-pale:#CADEEF;
  --blue-mist:#E8F1F8;
  --red:#EB3D1F;
  --coral:#EC4F4E;
  --pink:#F09395;
  --ink:#1d1d1f;
  --dark:#141414;
  --line:#dfe3e8;
}
*{margin:0;padding:0;box-sizing:border-box}
html,body{width:1200px;height:3974px;overflow:hidden;background:#fff}
body{position:relative;font-family:"Quicksand",sans-serif;color:var(--ink)}
.abs{position:absolute}
.head-font{font-family:"Montserrat",sans-serif}

/* brand name */
.brand-name{font-family:"Montserrat",sans-serif;font-weight:700;font-size:36px;letter-spacing:1px;color:#2a2a2a;line-height:1}
.brand-top{left:0;width:1200px;top:48px;text-align:center}
.brand-foot{left:93px;top:3860px;color:#fff}

/* hero */
.band{left:0;width:1200px;background:var(--blue)}
.hero-band{top:366px;height:577px}
.hero-photo{left:105px;top:133px;width:992px;height:495px;background:linear-gradient(180deg,#c9b58a 0%,#e7d7a9 14%,#3c5a86 30%,#24426f 65%,#5f7a3c 100%)}
.hero-corner{left:1010px;top:125px;width:94px;height:96px;border-top:2px solid var(--red);border-right:2px solid var(--red)}
.hero-title{top:684px;width:1200px;text-align:center;color:#fff;font-weight:600;font-size:31px;letter-spacing:-.6px}
.hero-sub{top:745px;width:1200px;text-align:center;color:#fff;font-weight:600;font-size:27px;letter-spacing:-.5px}
.hero-sub span{color:var(--pink)}
.btn{top:828px;height:56px;display:flex;align-items:center;justify-content:center;font-family:"Montserrat",sans-serif;font-weight:500;font-size:19px}
.btn-solid{left:325px;width:318px;background:#fff;color:var(--blue)}
.btn-ghost{left:669px;width:206px;border:2px solid #fff;color:#fff}

/* intro */
.intro-frame{left:77px;top:1054px;width:452px;height:606px;background:var(--red)}
.intro-photo{left:84px;top:1050px;width:445px;height:596px;background:linear-gradient(180deg,#e4e4e4,#bdbdbd);border:2px solid #fff}
.greet{left:598px;top:1050px;font-weight:600;font-size:28px;color:#222}
.greet span{color:var(--blue)}
.copy{font-size:23px;line-height:46.5px;color:#2b2b2b}
.intro-copy{left:598px;top:1116px;width:530px}
.copy p{margin-bottom:26px}

/* brands */
.brands-band{top:1775px;height:642px}
.brand-tile{width:231px;height:123px;background:#fff;display:flex;align-items:center;justify-content:center;gap:10px;font-family:"Quicksand",sans-serif;font-weight:600;font-size:38px;color:var(--blue);letter-spacing:2px}
.tile-dot{width:20px;height:20px;border-radius:50%;background:var(--blue)}
.product-box{left:430px;top:1956px;width:340px;height:293px;background:#3f7fc6}
.product-img{left:470px;top:2000px;width:260px;height:200px;background:linear-gradient(90deg,#e9edf1 0%,#f7f8fa 55%,#d7dde4 100%)}

/* install */
.install-copy{left:76px;top:2550px;width:505px}
.cta-line{color:var(--blue-mid);margin-top:-4px}
.install-frame{left:681px;top:2531px;width:440px;height:373px;background:var(--red)}
.install-photo{left:674px;top:2525px;width:440px;height:373px;background:linear-gradient(180deg,#cfe0ef 0%,#7fa1c6 30%,#2b4a78 65%,#6a6a4a 100%);border:2px solid #fff}

/* benefits */
.why{top:3014px;width:1200px;text-align:center;font-weight:600;font-size:29px;color:#1a1a1a;letter-spacing:-.5px}
.why span{color:var(--blue)}
.card{background:#fff;border:1.5px solid var(--line);box-shadow:0 2px 6px rgba(0,0,0,.05);display:flex;align-items:center;padding:0 16px 0 14px;gap:16px}
.card p{font-size:20px;line-height:42px;color:#222}
.card svg{flex:0 0 auto;width:50px;height:50px}
.card-a{left:76px;top:3111px;width:336px;height:224px}
.card-b{left:432px;top:3111px;width:335px;height:224px}
.card-c{left:788px;top:3111px;width:335px;height:224px;padding-left:26px}
.card-d{left:254px;top:3367px;width:335px;height:177px}
.card-e{left:611px;top:3367px;width:334px;height:177px;padding-left:26px}

/* footer */
.sign-band{top:3659px;height:121px;display:flex;align-items:center;justify-content:center;color:#fff;font-family:"Montserrat",sans-serif;font-weight:600;font-size:24px;letter-spacing:-.4px}
.foot{left:0;top:3780px;width:1200px;height:194px;background:var(--dark)}
.copyright{right:92px;top:3862px;color:#fff;font-family:"Montserrat",sans-serif;font-weight:500;font-size:18px}
</style>
</head>
<body>

<div class="abs brand-name brand-top">CORVEL ENERGY</div>

<div class="abs band hero-band"></div>
<div class="abs hero-photo" role="img" aria-label="Large solar farm with rows of panels under a rising sun"></div>
<div class="abs hero-corner"></div>
<h1 class="abs hero-title head-font">FEDERAL GOVERNMENT BATTERY SUBSIDY IS COMING</h1>
<h2 class="abs hero-sub head-font">MAXIMISE YOUR <span>SOLAR SAVINGS</span></h2>
<a class="abs btn btn-solid">SECURE MY BATTERY NOW</a>
<a class="abs btn btn-ghost">BEAT THE RUSH</a>

<div class="abs intro-frame"></div>
<div class="abs intro-photo" role="img" aria-label="Home battery inverter and switchboard installed on a wall"></div>
<div class="abs greet head-font">HI <span>HARLAN,</span></div>
<div class="abs copy intro-copy">
  <p>Great news! With the federal election now decided, the Federal Government’s Home Battery Subsidy Program is officially on the way.</p>
  <p>While the scheme hasn’t formally launched yet, it’s guaranteed—and like the solar rebate before it, the subsidy reduces each year, so the earlier you install, the more you’ll save.</p>
  <p>Crucially, the subsidy is only available once per household, so it makes sense to install a system that fully meets your home's battery needs right from the start.</p>
</div>

<div class="abs band brands-band"></div>
<div class="abs brand-tile" style="left:179px;top:1846px"><span class="tile-dot"></span>QMP</div>
<div class="abs brand-tile" style="left:791px;top:1846px">VELTO</div>
<div class="abs brand-tile" style="left:179px;top:2224px;font-size:30px;letter-spacing:0">TervoPWR</div>
<div class="abs brand-tile" style="left:791px;top:2224px;color:#e6891e;font-size:30px">BRIMLITE</div>
<svg class="abs" style="left:0;top:1775px" width="1200" height="642" aria-hidden="true">
  <g stroke="var(--red)" stroke-width="1.5" fill="none">
    <path d="M410 196 L430 214"/><path d="M790 196 L770 214"/>
    <path d="M410 450 L430 430"/><path d="M790 450 L770 430"/>
  </g>
</svg>
<div class="abs product-box"></div>
<div class="abs product-img" role="img" aria-label="Stacked battery modules beside a hybrid inverter"></div>

<div class="abs copy install-copy">
  <p>If you’ve already installed solar with us, now is the ideal time to complete your setup with a battery system designed to maximise your return—and take full advantage of this one-off federal subsidy.</p>
  <p class="cta-line">Call us today or reply to this email to secure your spot and beat the rush.</p>
</div>
<div class="abs install-frame"></div>
<div class="abs install-photo" role="img" aria-label="Two engineers in safety vests inspecting solar panels"></div>

<h3 class="abs why head-font">WHY ADD A BATTERY TO YOUR EXISTING <span>SOLAR SYSTEM NOW?</span></h3>

<div class="abs card card-a">
  <svg viewBox="0 0 50 50" fill="none" stroke="var(--blue-mid)" stroke-width="1.6"><circle cx="25" cy="25" r="22" stroke-dasharray="3 3"/><path d="M25 13a8 8 0 0 0-5 14v4h10v-4a8 8 0 0 0-5-14z"/><path d="M21 35h8M22 38h6"/></svg>
  <p>Store your excess solar energy instead of sending it back to the grid for low feed-in tariffs</p>
</div>
<div class="abs card card-b">
  <svg viewBox="0 0 50 50" fill="none" stroke="var(--blue-mid)" stroke-width="1.6"><circle cx="9" cy="9" r="4"/><path d="M18 14h26l-6 20H12z M21 14l-4 20 M27 14l-3 20 M33 14l-2 20 M40 14l-3 20 M15 24h27"/><path d="M4 44v-8h12v8z M24 44v-10"/></svg>
  <p>Use your stored solar power at night, when electricity prices are highest (typically 5–8pm)</p>
</div>
<div class="abs card card-c">
  <svg viewBox="0 0 50 50" fill="none" stroke="var(--blue-mid)" stroke-width="1.6"><path d="M10 4h24v40H10z"/><path d="M15 26h14M15 31h14M15 36h10"/><circle cx="22" cy="14" r="5"/><circle cx="36" cy="36" r="8"/><path d="M36 31v10M33 33h5a2 2 0 0 1 0 4h-4"/></svg>
  <p>Slash your power bills and avoid rising time-of-use charges</p>
</div>
<div class="abs card card-d">
  <svg viewBox="0 0 50 50" fill="none" stroke="var(--blue-mid)" stroke-width="1.6"><circle cx="9" cy="9" r="4"/><path d="M18 14h26l-6 20H12z M21 14l-4 20 M27 14l-3 20 M33 14l-2 20 M40 14l-3 20 M15 24h27"/><path d="M4 44v-8h12v8z M24 44v-10"/></svg>
  <p>Increase your self sufficiency &amp; long term energy security</p>
</div>
<div class="abs card card-e">
  <svg viewBox="0 0 50 50" fill="none" stroke="var(--blue-mid)" stroke-width="1.6"><path d="M10 4h24v40H10z"/><path d="M15 26h14M15 31h14M15 36h10"/><circle cx="22" cy="14" r="5"/><circle cx="36" cy="36" r="8"/><path d="M36 31v10M33 33h5a2 2 0 0 1 0 4h-4"/></svg>
  <p>Protect your home from power outages</p>
</div>

<div class="abs band sign-band">LET YOUR SOLAR WORK SMARTER FOR YOUR HOME, THE CORVEL ENERGY TEAM</div>
<div class="abs foot"></div>
<div class="abs brand-name brand-foot">CORVEL ENERGY</div>
<div class="abs copyright">@2025 COPYRIGHTS</div>

</body>
</html>
```